GUARANTEED! Simple website for independent event planner and consultant...

I need a website that is no more than 5 or 6 pages to illustrate who I am and what I can offer to groups who book hotels for meetings and conferences. I have 20 years of experience planning meetings within hotels and I am now ready to go out on my own and help clients choose venues, negotiate contracts and plan effective meetings. I will focus on clients planning meetings in the mountains of Colorado but I am willing to travel as well. I want to work with a person who is collaborative and can direct me on what they need to move the project along quickly. I already have my logo, a hosting site and work e-mail address. Also, I recently hired a photographer to do head shots. Lastly, it important for me to be able to talk on the phone or skype with this person, as needed and I must be able to make changes to my site down the road when necessary...

Target Market(s)

Corporate Groups

Industry/Entity Type

Event Planning

Coding

Coded - Design and coding required

Number of Pages Required

5+ page

Font styles to use
Sans Serif

Requirements
Must have
• About me page, event planning services offered page, task force and consulting work page, testimonials page, page for blogs, page to contact me/request a proposal. May need advice on what else I need...
Nice to have
• I want it to look sharp and professional. I want people to look at my site and know immediately that they can trust me and the work I can do.
• I don't want it to look like it is over the top as I am not a HUGE company but I do want it to be professional and easy to view and navigate.
Should not have
• Bright colors
• My logo is bright orange and black. I have also used dark grey and orange. See below:
• Orange:
• C = 0
• M = 64
• Y = 100
• K = 0
• Gray:
• C = 67
• M = 60
• Y = 59
• K = 45
• Font: Gotham Book and Gotham Bold

```html
<!DOCTYPE html>
<html lang="en">
<head>
<meta charset="utf-8">
<title>Alder Event Management</title>
<link rel="stylesheet" href="https://fonts.googleapis.com/css2?family=Montserrat:wght@400;500;600;700&display=swap">
<style>
:root{
  --orange:#f47920;
  --ink:#2f2f2f;
  --text:#444;
  --muted:#8a8a8a;
  --grey-band:#efefef;
  --grey-soft:#f4f4f4;
  --footer:#464646;
  --line:#cfcfcf;
  --white:#fff;
}
*{margin:0;padding:0;box-sizing:border-box}
html,body{width:1200px;height:2889px;overflow:hidden}
body{font-family:"Montserrat",Arial,sans-serif;color:var(--text);background:var(--white);position:relative}
.abs{position:absolute}
.accent{color:var(--orange);font-weight:700}

/* header */
.site-header{position:absolute;left:0;top:0;width:1200px;height:92px;background:var(--white)}
.brand-name{position:absolute;left:58px;top:34px;font-size:17px;font-weight:600;color:var(--ink);letter-spacing:.3px;white-space:nowrap}
.main-nav{position:absolute;left:289px;top:0;height:92px;display:flex;align-items:center}
.main-nav a{font-size:11px;font-weight:600;color:var(--ink);text-decoration:none;letter-spacing:.5px;margin-right:21px;white-space:nowrap}
.main-nav a.active{color:var(--orange);border:1.5px solid var(--orange);border-top:0;padding:12px 14px}
.btn-proposal{position:absolute;left:965px;top:27px;width:175px;height:37px;background:var(--orange);color:var(--white);font-size:11px;font-weight:600;letter-spacing:.8px;display:flex;align-items:center;justify-content:center}

/* hero */
.hero{position:absolute;left:0;top:92px;width:1200px;height:553px;background:linear-gradient(120deg,#4b4f55,#6f7378 45%,#55585c)}
.hero-shade{position:absolute;inset:0;background:rgba(30,30,35,.35)}
.hero-frame{position:absolute;left:491px;top:135px;width:218px;height:283px;border:2px solid var(--orange);text-align:center;color:var(--white)}
.hero-kicker{margin-top:30px;font-size:12px;letter-spacing:1.5px}
.hero-title{margin:28px -40px 0;font-size:34px;font-weight:700;line-height:1.35;letter-spacing:1px;white-space:nowrap}
.hero-more{margin-top:26px;font-size:11.5px;font-weight:600;letter-spacing:1.2px}
.hero-arrow{position:absolute;top:264px;width:56px;height:24px;border:2px solid var(--orange);display:flex;align-items:center;justify-content:center}
.hero-arrow.next{background:var(--orange)}

/* about */
.about{position:absolute;left:0;top:645px;width:1200px;height:520px;background:var(--grey-band)}
.about-bar-v{position:absolute;left:87px;top:0;width:29px;height:520px;background:var(--orange)}
.about-bar-h{position:absolute;left:116px;top:0;width:381px;height:25px;background:var(--orange)}
.section-title{font-size:27px;font-weight:400;color:var(--ink);white-space:nowrap}
.title-rule{height:1px;background:var(--line)}
.about-copy{position:absolute;left:175px;top:182px;width:500px;font-size:13px;line-height:1.65;color:var(--ink)}
.about-copy.soft{top:262px;color:var(--muted)}
.btn-outline{position:absolute;border:1.5px solid var(--orange);color:var(--ink);font-size:11.5px;font-weight:600;letter-spacing:1.2px;display:flex;align-items:center;justify-content:center;gap:10px}

/* services */
.services{position:absolute;left:0;top:1165px;width:1200px;height:445px;background:var(--white)}
.photo{position:absolute}
.service-list{position:absolute;left:643px;top:181px;list-style:none}
.service-list li{display:flex;align-items:center;gap:14px;font-size:15px;color:var(--text);height:28px}
.btn-solid{position:absolute;background:var(--orange);color:var(--white);font-size:12px;font-weight:700;letter-spacing:.8px;display:flex;align-items:center;justify-content:center}

/* testimonials */
.testimonials{position:absolute;left:0;top:1610px;width:1200px;height:432px;background:var(--grey-soft)}
.view-all{position:absolute;left:919px;font-size:11.5px;font-weight:600;letter-spacing:1.3px;color:var(--ink);display:flex;align-items:center;gap:10px}
.quote-card{position:absolute;top:172px;width:412px;height:204px;border:1.5px solid #d6d6d6;background:var(--grey-soft);padding:54px 28px 0}
.avatar{position:absolute;top:142px;width:60px;height:60px;border-radius:50%;background:#3a3a3a;border:2px solid var(--white)}
.quote-name{font-size:15px;font-weight:700;color:var(--ink)}
.quote-name span{font-size:12px;font-weight:500}
.quote-text{margin-top:12px;font-size:13px;line-height:1.65;color:var(--muted)}
.circle-arrow{position:absolute;width:26px;height:26px;border-radius:50%;border:1.5px solid #9a9a9a;display:flex;align-items:center;justify-content:center}

/* blog */
.blog{position:absolute;left:0;top:2042px;width:1200px;height:524px;background:var(--white)}
.post-date{position:absolute;font-size:12.5px;font-weight:700;letter-spacing:1.3px;color:var(--orange)}
.post-title{position:absolute;width:412px;font-size:23px;line-height:1.25;color:var(--ink)}

/* footer */
.site-footer{position:absolute;left:0;top:2566px;width:1200px;height:323px;background:var(--footer);color:#d5d5d5}
.footer-brand{position:absolute;left:87px;top:60px;width:260px;font-size:28px;font-weight:600;line-height:1.25;color:var(--white)}
.footer-small{position:absolute;font-size:11px;line-height:1.9}
.footer-title{position:absolute;font-size:21px;font-weight:400;color:var(--white)}
.footer-rule{position:absolute;height:1px;background:#6a6a6a}
.footer-text{position:absolute;font-size:13px;line-height:1.6}
.social{position:absolute;top:232px;width:32px;height:32px;border-radius:50%;border:1.5px solid #bdbdbd}
.email-field{position:absolute;left:815px;top:175px;width:296px;height:36px;background:#5a5a5a;border:1px solid #777;font-size:12px;color:#cfcfcf;padding:0 12px;display:flex;align-items:center}
.btn-send{position:absolute;left:815px;top:231px;width:111px;height:36px;border:1.5px solid var(--orange);color:var(--white);font-size:12px;font-weight:700;letter-spacing:1.2px;display:flex;align-items:center;justify-content:center;gap:8px}
</style>
</head>
<body>

<header class="site-header">
  <div class="brand-name">Alder Event Management</div>
  <nav class="main-nav">
    <a class="active">HOME</a><a>ABOUT US</a><a>SERVICES</a><a>CONSULTING WORK</a><a>TESTIMONIALS</a><a>BLOG</a><a>CONTACT</a>
  </nav>
  <div class="btn-proposal">REQUEST A PROPOSAL</div>
</header>

<section class="hero">
  <div class="hero-shade" role="img" aria-label="Business people shaking hands across a meeting table"></div>
  <div class="hero-frame">
    <div class="hero-kicker">BOOK HOTELS</div>
    <div class="hero-title">MEETINGS<br>&amp;<br>CONFERENCES</div>
    <div class="hero-more">EXPLORE MORE &nbsp;→</div>
  </div>
  <div class="hero-arrow" style="left:31px"><svg width="18" height="10" viewBox="0 0 18 10"><path d="M17 5H2M6 1L2 5l4 4" fill="none" stroke="#fff" stroke-width="1.6"/></svg></div>
  <div class="hero-arrow next" style="left:1113px"><svg width="18" height="10" viewBox="0 0 18 10"><path d="M1 5h15M12 1l4 4-4 4" fill="none" stroke="#fff" stroke-width="1.6"/></svg></div>
</section>

<section class="about">
  <div class="about-bar-v"></div>
  <div class="about-bar-h"></div>
  <h2 class="section-title abs" style="left:173px;top:92px">Maren <span class="accent">Collins</span></h2>
  <div class="title-rule abs" style="left:148px;top:145px;width:305px"></div>
  <p class="about-copy">I have 20 years of experience planning meetings within hotels and I am now ready to go out on my own and help clients choose venues, negotiate contracts and plan effective meetings.</p>
  <p class="about-copy soft">Every event starts with listening. From the first call to the final session, I handle venue searches, contract terms, room blocks and schedules so your team can focus on the meeting itself, wherever it takes place...</p>
  <div class="btn-outline" style="left:175px;top:387px;width:185px;height:37px">DISCOVER MORE <span>→</span></div>
  <svg class="abs" style="left:690px;top:60px" width="440" height="420" viewBox="0 0 440 420">
    <polygon points="163,8 250,95 163,182 76,95" fill="#9aa3a8" role="img" aria-label="Headshot of the planner in a dark blazer"/>
    <polygon points="123,176 239,292 123,408 7,292" fill="#3c3c3c" role="img" aria-label="Close headshot of the planner smiling"/>
    <polygon points="308,128 419,239 308,350 197,239" fill="#c9cfc9" role="img" aria-label="Outdoor portrait of the planner"/>
  </svg>
</section>

<section class="services">
  <div class="photo" style="left:87px;top:56px;width:498px;height:331px;background:linear-gradient(135deg,#8e8fa6,#b7b4c4 50%,#6c6a78)" role="img" aria-label="Planner presenting to a team around a meeting table"></div>
  <h2 class="section-title abs" style="left:639px;top:48px">Our <span class="accent">Services</span></h2>
  <div class="title-rule abs" style="left:612px;top:104px;width:178px"></div>
  <h3 class="abs" style="left:640px;top:128px;font-size:22px;font-weight:400;color:var(--ink);white-space:nowrap">Event Planning and Consulting Services</h3>
  <ul class="service-list">
    <li><svg width="14" height="14" viewBox="0 0 14 14"><rect x="1" y="3" width="10" height="10" fill="none" stroke="#f47920" stroke-width="1.4"/><path d="M3.5 7.5l2.5 2.5 6-7" fill="none" stroke="#f47920" stroke-width="1.6"/></svg>Professional Meeting Events</li>
    <li><svg width="14" height="14" viewBox="0 0 14 14"><rect x="1" y="3" width="10" height="10" fill="none" stroke="#f47920" stroke-width="1.4"/><path d="M3.5 7.5l2.5 2.5 6-7" fill="none" stroke="#f47920" stroke-width="1.6"/></svg>Personal Gathering Events</li>
    <li><svg width="14" height="14" viewBox="0 0 14 14"><rect x="1" y="3" width="10" height="10" fill="none" stroke="#f47920" stroke-width="1.4"/><path d="M3.5 7.5l2.5 2.5 6-7" fill="none" stroke="#f47920" stroke-width="1.6"/></svg>Tour and Travels Consulting</li>
    <li><svg width="14" height="14" viewBox="0 0 14 14"><rect x="1" y="3" width="10" height="10" fill="none" stroke="#f47920" stroke-width="1.4"/><path d="M3.5 7.5l2.5 2.5 6-7" fill="none" stroke="#f47920" stroke-width="1.6"/></svg>Help to choose Venues for Event</li>
    <li><svg width="14" height="14" viewBox="0 0 14 14"><rect x="1" y="3" width="10" height="10" fill="none" stroke="#f47920" stroke-width="1.4"/><path d="M3.5 7.5l2.5 2.5 6-7" fill="none" stroke="#f47920" stroke-width="1.6"/></svg>Book Hotels for Events</li>
  </ul>
  <div class="btn-solid" style="left:639px;top:351px;width:297px;height:36px">CONTACT&nbsp;<span style="color:#2f2f2f">MAREN COLLINS</span>&nbsp;NOW!</div>
</section>

<section class="testimonials">
  <h2 class="section-title abs" style="left:175px;top:50px">What Our <span class="accent">Clients Say</span></h2>
  <div class="title-rule abs" style="left:148px;top:104px;width:174px"></div>
  <div class="view-all" style="top:64px">VIEW ALL <span>→</span></div>
  <div class="quote-card" style="left:175px">
    <div class="quote-name">Adam Reed, <span>Arch Worker</span></div>
    <p class="quote-text">Lorem Ipsum has been the industry's standard dummy text ever since the 1500s, when an unknown printer took a galley of type and scrambled it to make a type...</p>
  </div>
  <div class="avatar" style="left:203px" role="img" aria-label="Client portrait"></div>
  <div class="quote-card" style="left:612px">
    <div class="quote-name">Lena Morrow, <span>Manager</span></div>
    <p class="quote-text">Lorem Ipsum has been the industry's standard dummy text ever since the 1500s, when an unknown printer took a galley of type and scrambled it to make a type...</p>
  </div>
  <div class="avatar" style="left:640px" role="img" aria-label="Client portrait"></div>
  <div class="circle-arrow" style="left:118px;top:259px"><svg width="8" height="10" viewBox="0 0 8 10"><path d="M6 1L2 5l4 4" fill="none" stroke="#9a9a9a" stroke-width="1.5"/></svg></div>
  <div class="circle-arrow" style="left:1056px;top:259px;border-color:var(--orange)"><svg width="8" height="10" viewBox="0 0 8 10"><path d="M2 1l4 4-4 4" fill="none" stroke="#f47920" stroke-width="1.5"/></svg></div>
</section>

<section class="blog">
  <h2 class="section-title abs" style="left:175px;top:50px">Our Latest <span class="accent">Blog</span></h2>
  <div class="title-rule abs" style="left:148px;top:104px;width:174px"></div>
  <div class="view-all" style="top:64px;color:var(--orange)">VIEW ALL <span>→</span></div>
  <div class="photo" style="left:175px;top:140px;width:412px;height:229px;background:linear-gradient(135deg,#8fa0b3,#c8d0d8 55%,#7d8a96)" role="img" aria-label="Colleagues discussing around a laptop"></div>
  <div class="photo" style="left:612px;top:140px;width:413px;height:229px;background:linear-gradient(135deg,#b9b9b9,#dedede 55%,#8e8e8e)" role="img" aria-label="Speaker addressing a seated audience"></div>
  <div class="post-date" style="left:175px;top:396px">APRIL 26, 2017</div>
  <div class="post-title" style="left:175px;top:424px">Contrary to popular belief looked up one of the more...</div>
  <div class="post-date" style="left:612px;top:396px">MAY 15, 2017</div>
  <div class="post-title" style="left:612px;top:424px;text-decoration:underline;text-decoration-color:#bbb;text-underline-offset:5px">Contrary to popular belief looked up one of the more...</div>
  <div class="circle-arrow" style="left:118px;top:241px"><svg width="8" height="10" viewBox="0 0 8 10"><path d="M6 1L2 5l4 4" fill="none" stroke="#9a9a9a" stroke-width="1.5"/></svg></div>
  <div class="circle-arrow" style="left:1056px;top:241px"><svg width="8" height="10" viewBox="0 0 8 10"><path d="M2 1l4 4-4 4" fill="none" stroke="#9a9a9a" stroke-width="1.5"/></svg></div>
</section>

<footer class="site-footer">
  <div class="footer-brand">Alder Event Management</div>
  <div class="footer-small" style="left:89px;top:226px">© 2017 <span style="color:var(--orange)">ALDER EVENT MANAGEMENT</span><br>All right reserved.</div>

  <h3 class="footer-title" style="left:437px;top:50px">Contact <span class="accent">Us</span></h3>
  <div class="footer-rule" style="left:410px;top:94px;width:206px"></div>
  <p class="footer-text" style="left:439px;top:120px;width:340px">4410 Summit Ridge Road Pinecrest,<br>CO 80000</p>
  <p class="footer-text" style="left:439px;top:170px;font-size:15px;color:var(--white);font-weight:600"><span style="color:var(--orange)">Call Us:</span> 555.014.0199</p>
  <p class="footer-text" style="left:439px;top:194px;text-decoration:underline">maren@aldereventmanagement.com</p>
  <div class="social" style="left:439px"></div>
  <div class="social" style="left:481px;background:#d5d5d5"></div>
  <div class="social" style="left:523px"></div>
  <div class="social" style="left:566px"></div>

  <h3 class="footer-title" style="left:815px;top:50px">Sign Up <span class="accent">Newsletter</span></h3>
  <div class="footer-rule" style="left:788px;top:94px;width:206px"></div>
  <p class="footer-text" style="left:817px;top:114px;width:310px">You Want to get Update about anything News? Join our newslette</p>
  <div class="email-field">Enter Your Email...</div>
  <div class="btn-send">SEND <span>→</span></div>
</footer>

</body>
</html>
```